Landscaping Company Flyer Design Project

I need a flyer design for a landscaping company based in Mokena, Illinois called Brightfold Yard & Garden. These flyers will be distributed door to door throughout the community. I want a design that is simple to read and allows the eye to flow along through it, nothing crammed. My logo is attached and would be nice to have on there, sometimes I take the tree off the top of logo to use which you can do as well if preferred. I also attached some pictures which may or may not be used depending on what you think. Some important information I would like on there is: 815-342-9186, company name, BrtfldYard.com, free estimates. fully insured. I would also like to list some services on there such as: Landscape Design & Construction, Lawn Maintenance, Fertilization & Weed Control, Hardscape Construction, Bush Trimming, Aeration, Thatch Removal, Mulch & Rock Installation, New Lawn Installation, Clean-Ups, and more. A company slogan I like to use sometimes is Let Your Yard Find the Brightfold Touch. Also I like to write Dependable professionals dedicated to the quality of your property. One important thing I definitely want on there is either in the form of a coupon or just written somewhere where it will pop out is : Let us earn your business. Call now and get your first cut free of charge. I have a lot of different logo sizes and different formats such as vector or .pdf if needed, so let me know. Also I would like the flyer to be standard paper size 8.5X11

```html
<!DOCTYPE html>
<html lang="en">
<head>
<meta charset="utf-8">
<title>Brightfold Yard &amp; Garden Flyer</title>
<link rel="stylesheet" href="https://fonts.googleapis.com/css2?family=Tinos:wght@400;700&display=swap">
<style>
  :root {
    --page-bg: #ece8e2;
    --green-deep: #0f3f17;
    --green-dark: #1c5a22;
    --green-mid: #2d7a2c;
    --green-light: #7cc142;
    --green-lime: #8ccf3f;
    --text-light: #8fd14a;
    --white: #ffffff;
    --ink: #1c2a12;
  }
  * { margin: 0; padding: 0; box-sizing: border-box; }
  html, body { width: 1200px; height: 900px; overflow: hidden; }
  body {
    background: var(--page-bg);
    font-family: "Tinos", "Times New Roman", serif;
    position: relative;
  }
  .flyer {
    position: absolute;
    left: 278px; top: 33px;
    width: 643px; height: 834px;
    background: radial-gradient(ellipse at 50% 70%, var(--green-mid) 0%, var(--green-dark) 55%, var(--green-deep) 100%);
    box-shadow: 0 6px 18px rgba(0,0,0,.25);
    overflow: hidden;
  }
  .header {
    position: absolute; left: 0; top: 0; width: 100%; height: 120px;
    background: linear-gradient(180deg, var(--green-deep), var(--green-dark));
  }
  .brand {
    position: absolute; left: 36px; top: 46px;
    display: flex; align-items: center; gap: 10px;
    color: var(--white); font-size: 20px; font-weight: 700;
    line-height: 1.1; width: 170px;
  }
  .brand-mark {
    width: 14px; height: 14px; border-radius: 50%;
    background: var(--green-lime); flex: none;
  }
  .contact {
    position: absolute; right: 32px; top: 34px;
    text-align: right; color: var(--text-light);
    font-size: 21px; line-height: 1.3;
  }
  .stripe-top {
    position: absolute; left: 0; top: 120px; width: 100%; height: 8px;
    background: var(--green-light);
  }
  .photo {
    position: absolute;
    background: linear-gradient(180deg, #8a8478 0%, #6e7a52 45%, #4f8a32 75%, #3d7a26 100%);
  }
  .photo-main { left: 0; top: 128px; width: 643px; height: 265px; }
  .photo-small {
    border: 5px solid var(--white);
    box-shadow: 0 3px 8px rgba(0,0,0,.35);
  }
  .photo-garden { left: -5px; top: 386px; width: 245px; height: 134px;
    background: linear-gradient(160deg, #4f7d34, #7aa23c 50%, #3d6b28); }
  .photo-brick { left: 200px; top: 430px; width: 243px; height: 136px;
    background: linear-gradient(180deg, #9a5a42 0%, #8a4c3a 50%, #3f7a2a 80%, #4d8a30 100%); z-index: 2; }
  .photo-steps { left: 406px; top: 386px; width: 242px; height: 134px;
    background: linear-gradient(160deg, #3f6e2a, #6c8c44 55%, #b9a47c); }
  .copy {
    position: absolute; left: 0; top: 578px; width: 100%;
    text-align: center;
  }
  .slogan { color: var(--text-light); font-size: 26px; font-weight: 400; line-height: 1.2; }
  .tagline { color: var(--text-light); font-size: 17px; margin-top: 6px; }
  .services {
    list-style: none; margin-top: 14px;
    color: var(--white); font-size: 18.5px; line-height: 22px;
  }
  .services .sep { display: inline-block; width: 1px; height: 12px; background: var(--white); margin: 0 6px; vertical-align: 0; }
  .stripe-bottom {
    position: absolute; left: 0; top: 757px; width: 100%; height: 6px;
    background: var(--green-light);
  }
  .stripe-bottom.dark { top: 763px; height: 8px; background: var(--green-deep); }
  .offer {
    position: absolute; left: 0; top: 771px; width: 100%; height: 63px;
    background: linear-gradient(180deg, var(--green-lime), #74b834);
    display: flex; align-items: center; justify-content: center;
    color: var(--ink); font-size: 18px;
  }
</style>
</head>
<body>
  <article class="flyer">
    <header class="header">
      <div class="brand"><span class="brand-mark"></span><span>Brightfold Yard &amp; Garden</span></div>
      <div class="contact">
        <p>Ph: 815-342-9186</p>
        <p>www.BrtfldYard.com</p>
      </div>
    </header>
    <div class="stripe-top"></div>

    <div class="photo photo-main" role="img" aria-label="Photo of a large stone-and-stucco home with a curved walkway, manicured lawn and trimmed shrub beds"></div>
    <div class="photo photo-small photo-garden" role="img" aria-label="Photo of a garden path bordered by yellow lilies and flower beds"></div>
    <div class="photo photo-small photo-steps" role="img" aria-label="Photo of stone garden steps with lush plantings and purple flowers"></div>
    <div class="photo photo-small photo-brick" role="img" aria-label="Photo of a brick house with rounded boxwood shrubs and lawn"></div>

    <section class="copy">
      <h1 class="slogan">Let Your Yard Find the Brightfold Touch</h1>
      <p class="tagline">Dependable professionals dedicated to the quality of your property</p>
      <ul class="services">
        <li>Landscape Design &amp; Construction Lawn Maintenance</li>
        <li>Fertilization &amp; Weed Control<span class="sep"></span>Hardscape Construction<span class="sep"></span>Bush Trimming</li>
        <li>Aeration<span class="sep"></span>Thatch Removal<span class="sep"></span>Mulch &amp; Rock Installation</li>
        <li>New Lawn Installation<span class="sep"></span>Clean-Ups, and more</li>
      </ul>
    </section>

    <div class="stripe-bottom"></div>
    <div class="stripe-bottom dark"></div>
    <footer class="offer">Let us earn your business. Call now and get your first cut free of charge.</footer>
  </article>
</body>
</html>
```